Brightwell Acupuncture Studio Website Design

We are working with Brightwell Acunpuncture Studio. They are a local Chinese medicine and acupuncture studio and in need of a new website design.

Some sites to use for inspiration:

https://marbleriveracupuncture.example
https://cedarglowacupuncture.example
https://quietharborclinic.example
https://emberfieldacupuncture.example
https://fernhollowclinic.example

Thank you for taking the time to consider designing a website for us. We are web developers based in Stockton, CA, USA. Most of our projects go through the same process. Understanding this process may help you win a project with us. We custom-code all of our websites in-house. We don’t have any requirements as to what tools you use for your design, but we prefer Figma files. For any design that we label as four-stars, we send it to the client for review. The client picks the final design they want us to use. Once we complete this process, we will continue to show additional clients all the four-star sites and purchase them later. Your designs will have multiple chances to sell. For better chances of success, we ask that you follow these guidelines.

IMAGES:
If you use any images or icons in the design, we ask that you have a link to the asset so we can purchase the image/icon. Most of the designs we submit do not have the customer’s images on them unless they have some great images. Be creative; show us the feeling you are trying to portray with your image choices. Use any royalty-free site you choose. We subscribe to Vantrel and mainly use their images, but we can purchase images outside of Vantrel.

PLEASE NOTE: we will not submit designs to clients with watermarks on the images.

FONTS:
We ask that you identify the fonts used in the design. This can be done in a message if you want. We typically use Google Fonts and Vantrel Fonts.

CONTENT:
We're always open to different content and ideas. We often submit designs with stock images so the client can see our vision. We typically take pictures after the website launch to use their images with our vision. Lorem Ipsum is fine for paragraphs, but we ask that you write the headers in correct English. We want to be able to show the vision and identify the sections of the website.

INSPIRATION:
We typically add a couple of links in the brief of websites we like to help you get started in your design.

REVISIONS:
We do not often ask for revisions of the designs unless we see something in the design that may not appeal to the client. If there are slight changes that we want to make, we do that in the development process.

FEEDBACK:
We rarely give feedback on designs during the design process. We are working on many website projects and do not have the time to provide feedback. We usually respond if your request is well thought out and asks specific questions, but a note asking “feedback, please” usually goes unanswered.

```html
<!DOCTYPE html>
<html lang="en">
<head>
<meta charset="utf-8">
<title>Brightwell Acupuncture Studio</title>
<link href="https://fonts.googleapis.com/css2?family=Poppins:wght@400;500;600;700&display=swap" rel="stylesheet">
<style>
:root{
  --coral:#e0665f;
  --coral-dark:#b94a44;
  --navy:#232a35;
  --ink:#2b2b2b;
  --card:#f9eeee;
  --footer:#272c37;
  --white:#ffffff;
}
*{margin:0;padding:0;box-sizing:border-box}
html,body{width:1200px;height:3524px;overflow:hidden}
body{font-family:'Poppins',sans-serif;color:var(--ink);background:var(--white);position:relative}
.abs{position:absolute}
.btn{position:absolute;display:flex;align-items:center;justify-content:center;background:var(--coral);color:var(--white);font-weight:500;border-radius:26px;box-shadow:0 4px 0 var(--coral-dark);text-decoration:none}
.brand{font-weight:600;color:var(--navy);line-height:1.05}
/* header */
.header-brand{left:111px;top:42px;display:flex;align-items:center;gap:14px}
.header-brand .dot{width:52px;height:52px;border-radius:50%;background:var(--coral)}
.header-brand .brand{font-size:24px}
.phone{left:588px;top:33px;display:flex;align-items:center;gap:20px;font-weight:600;font-size:18px;color:var(--navy)}
.phone-icon{width:52px;height:52px;border-radius:50%;background:#fbe3e1;display:flex;align-items:center;justify-content:center}
.nav{position:absolute;top:108px;right:111px;display:flex;gap:35px;font-size:16px;font-weight:600;color:var(--navy)}
.nav .active{color:var(--coral)}
/* hero */
.hero-text{left:0;width:1200px;text-align:center;color:var(--white)}
.hero-title{top:300px;font-size:44px;line-height:53px}
.hero-title b{font-weight:700}
.hero-title span{font-weight:400}
.hero-sub{top:416px;font-size:21px;line-height:32px;font-weight:500;left:290px;width:620px}
/* about */
.about-mark{left:111px;top:850px;width:264px;height:320px}
.about-bar{left:371px;top:850px;width:9px;height:312px;background:var(--navy)}
.eyebrow{color:var(--coral);font-weight:500;font-size:26px}
.section-title{color:var(--navy);font-size:44px;line-height:53px}
.section-title b{font-weight:700}
.copy{font-size:18px;line-height:28.5px;color:var(--ink)}
.divider{left:111px;top:1378px;width:978px;height:2px;background:#cfcfcf}
/* services */
.services-title{left:0;width:1200px;top:1436px;text-align:center;font-size:50px;color:var(--navy)}
.card{position:absolute;width:475px;height:230px;background:var(--card);border-radius:28px 0 0 28px}
.card-photo{position:absolute;left:6px;top:6px;width:226px;height:218px;border-radius:24px 0 0 24px}
.card h3{position:absolute;left:256px;top:22px;font-size:17px;font-weight:600;color:var(--navy)}
.card p{position:absolute;left:256px;top:56px;width:200px;font-size:14px;line-height:22px;color:#444}
.card .btn{left:258px;top:160px;width:119px;height:37px;font-size:13px;border-radius:20px}
/* relief */
.relief{left:111px;top:2113px;width:978px;height:496px;border-radius:248px 248px 0 248px;background:linear-gradient(120deg,#ece8e4 0%,#e2c6ae 35%,#d7b195 55%,#ede7e1 85%);overflow:hidden}
.relief-circle{left:155px;top:2157px;width:410px;height:410px;border-radius:50%;background:var(--coral);color:var(--white);text-align:center}
/* journey */
.journey-photo{left:0;top:2658px;width:690px;height:537px;background:linear-gradient(90deg,#f3ede8 0%,#e8cdb8 35%,#efdccd 60%,#ffffff 100%)}
/* footer */
.footer{left:0;top:3243px;width:1200px;height:281px;background:var(--footer);color:var(--white)}
.foot-h{font-size:16px;font-weight:600;position:absolute;top:70px}
.foot-h::after{content:"";display:block;width:36px;height:1px;background:#8a8f99;margin-top:8px}
.foot-list{position:absolute;font-size:14px;line-height:31px}
.icon-dot{position:absolute;width:26px;height:26px;border-radius:50%;border:1px solid #8a8f99;display:flex;align-items:center;justify-content:center}
.social{position:absolute;width:32px;height:32px;border-radius:50%;background:var(--white)}
</style>
</head>
<body>

<!-- Header -->
<header>
  <div class="abs header-brand"><div class="dot"></div><div class="brand">Brightwell<br>Acupuncture Studio</div></div>
  <div class="abs phone">
    <div class="phone-icon">
      <svg width="22" height="22" viewBox="0 0 24 24" fill="none" stroke="#e0665f" stroke-width="2"><path d="M5 3h4l2 5-3 2a11 11 0 0 0 6 6l2-3 5 2v4a2 2 0 0 1-2 2A17 17 0 0 1 3 5a2 2 0 0 1 2-2z"/></svg>
    </div>
    <span>+1 000 000 0000</span>
  </div>
  <a class="btn" style="left:843px;top:33px;width:245px;height:48px;font-size:16px">Book Your Consultation</a>
  <nav class="nav">
    <span class="active">Home</span><span>About Brightwell</span><span>Our Services</span><span>Schedule/Book</span><span>Contact Us</span>
  </nav>
</header>

<!-- Hero -->
<section>
  <svg class="abs" style="left:0;top:161px" width="1200" height="620" viewBox="0 161 1200 620">
    <defs>
      <linearGradient id="heroTone" x1="0" y1="0" x2="1" y2="1">
        <stop offset="0" stop-color="#3a2a26"/>
        <stop offset="0.5" stop-color="#6b4a3c"/>
        <stop offset="1" stop-color="#a07a66"/>
      </linearGradient>
    </defs>
    <path d="M0,330 H1200 V560 Q600,1086 0,330 Z" fill="#e0665f"/>
    <path d="M0,161 H1200 V575 Q600,1012 0,356 Z" fill="url(#heroTone)" role="img" aria-label="Photo of a woman receiving facial acupuncture"/>
  </svg>
  <h1 class="abs hero-text hero-title"><b>Where Healing Begins &amp;</b><br><span>Harmony Follows</span></h1>
  <p class="abs hero-text hero-sub">Restore balance and wellness with personalized acupuncture and Chinese medicine treatments rooted in centuries of healing wisdom.</p>
  <a class="btn" style="left:477px;top:532px;width:245px;height:48px;font-size:16px">Book Your Consultation</a>
</section>

<!-- About -->
<section>
  <svg class="abs about-mark" viewBox="0 0 264 320"><circle cx="132" cy="160" r="120" fill="#e0665f"/></svg>
  <div class="abs about-bar"></div>
  <div class="abs eyebrow" style="left:422px;top:842px">About Brightwell</div>
  <h2 class="abs section-title" style="left:422px;top:878px;width:560px"><b>Natural Healing from</b><br>the Heart of Chinese<br>Medicine</h2>
  <p class="abs copy" style="left:422px;top:1051px;width:668px">At Brightwell Acupuncture Studio, we specialize in traditional Chinese medicine and modern acupuncture techniques to support your body’s natural healing process.</p>
  <p class="abs copy" style="left:422px;top:1145px;width:668px">Whether you're managing chronic pain, stress, or looking to enhance overall wellness, our licensed practitioners provide thoughtful, personalized care in a serene and welcoming environment.</p>
  <a class="btn" style="left:422px;top:1257px;width:143px;height:49px;font-size:16px">Learn More</a>
  <div class="abs divider"></div>
</section>

<!-- Services -->
<section>
  <h2 class="abs services-title">Our <b style="font-weight:700">Services</b></h2>

  <div class="card" style="left:111px;top:1540px">
    <div class="card-photo" role="img" aria-label="Photo of acupuncture needles on a client's back" style="background:linear-gradient(135deg,#c9a08a,#8e6a57)"></div>
    <h3>Acupuncture</h3>
    <p>Relieve pain, reduce stress, and restore balance with precise, therapeutic needling.</p>
    <a class="btn">Book Now</a>
  </div>
  <div class="card" style="left:614px;top:1540px">
    <div class="card-photo" role="img" aria-label="Photo of cupping therapy on a client's back" style="background:linear-gradient(135deg,#eae6e2,#c89b88)"></div>
    <h3>Cupping Therapy</h3>
    <p>Promote circulation and muscle recovery with time-tested suction therapy.</p>
    <a class="btn">Book Now</a>
  </div>
  <div class="card" style="left:111px;top:1798px">
    <div class="card-photo" role="img" aria-label="Photo of hands gathering fresh herbs" style="background:linear-gradient(135deg,#6b7a4a,#a7a68a)"></div>
    <h3>Herbal Medicine</h3>
    <p>Natural, customized herbal formulas to support internal healing.</p>
    <a class="btn">Book Now</a>
  </div>
  <div class="card" style="left:614px;top:1798px">
    <div class="card-photo" role="img" aria-label="Photo of a Tui Na massage session" style="background:linear-gradient(135deg,#b08a6a,#e4ddd8)"></div>
    <h3>Tui Na Massage</h3>
    <p>Restore physical alignment and reduce tension with traditional Chinese bodywork.</p>
    <a class="btn">Book Now</a>
  </div>
</section>

<!-- Relief -->
<section>
  <div class="abs relief" role="img" aria-label="Photo of acupuncture needles placed along a client's shoulders"></div>
  <div class="abs relief-circle">
    <h2 style="margin-top:60px;font-size:36px;line-height:44px;font-weight:700">Relief Starts<br><span style="font-weight:400">Here</span></h2>
    <p style="margin:12px auto 0;width:320px;font-size:17px;line-height:28.5px;font-weight:500">At Brightwell Acupuncture Studio, we believe healing is more than symptom relief—it’s about restoring the body’s natural balance and empowering you to thrive.</p>
  </div>
  <a class="btn" style="left:300px;top:2470px;width:118px;height:41px;font-size:14px;background:var(--white);color:var(--navy);box-shadow:0 4px 0 #c5c5c5">Book Now</a>
</section>

<!-- Journey -->
<section>
  <div class="abs journey-photo" role="img" aria-label="Photo of a practitioner placing acupuncture needles on a client's back"></div>
  <h2 class="abs section-title" style="left:600px;top:2706px"><b>Beginning</b><br>The Healing Journey</h2>
  <p class="abs copy" style="left:601px;top:2826px;width:490px">Founded on the principles of traditional Chinese medicine, our studio blends ancient wisdom with modern, evidence-based techniques to deliver personalized care for each client.</p>
  <p class="abs copy" style="left:601px;top:2946px;width:490px">Whether you're seeking relief from chronic pain, stress, digestive issues, or simply want to improve your overall wellness, we’re here to guide your healing journey with skill and compassion.</p>
  <a class="btn" style="left:601px;top:3088px;width:253px;height:50px;font-size:16px">Schedule an Apointment</a>
</section>

<!-- Footer -->
<footer class="abs footer">
  <div class="abs" style="left:111px;top:122px;display:flex;align-items:center;gap:12px">
    <div style="width:40px;height:40px;border-radius:50%;background:var(--coral)"></div>
    <div style="font-weight:600;font-size:19px;line-height:1.05">Brightwell<br>Acupuncture Studio</div>
  </div>
  <div class="abs" style="left:111px;top:204px;font-size:13px">© 2025 &nbsp; / &nbsp; All Rights Reserved</div>

  <div class="foot-h" style="left:377px">SITE MAP</div>
  <div class="foot-list" style="left:377px;top:110px">Home<br>About Brightwell<br>Our Services<br>Schedule/Book<br>Contact Us</div>

  <div class="foot-h" style="left:512px">CONTACT INFO</div>
  <div class="icon-dot" style="left:509px;top:107px"><svg width="12" height="12" viewBox="0 0 24 24" fill="#fff"><path d="M5 3h4l2 5-3 2a11 11 0 0 0 6 6l2-3 5 2v4a2 2 0 0 1-2 2A17 17 0 0 1 3 5a2 2 0 0 1 2-2z"/></svg></div>
  <div class="icon-dot" style="left:509px;top:143px"><svg width="12" height="12" viewBox="0 0 24 24" fill="#fff"><rect x="2" y="5" width="20" height="14" rx="2"/></svg></div>
  <div class="icon-dot" style="left:509px;top:179px"><svg width="12" height="12" viewBox="0 0 24 24" fill="#fff"><path d="M12 2a7 7 0 0 0-7 7c0 5 7 13 7 13s7-8 7-13a7 7 0 0 0-7-7z"/></svg></div>
  <div class="abs" style="left:551px;top:110px;font-size:14px;line-height:20px">+1 000 000 0000</div>
  <div class="abs" style="left:551px;top:146px;font-size:14px;line-height:20px">info@brightwellacupuncture.example</div>
  <div class="abs" style="left:551px;top:182px;font-size:14px;line-height:24px">123 Brightwell Acupuncture Studio<br>USA</div>

  <div class="foot-h" style="left:852px">SUBSCRIBE</div>
  <div class="abs" style="left:853px;top:105px;width:236px;height:36px;border-radius:18px;background:var(--white);overflow:hidden;display:flex">
    <div style="flex:1;font-size:11px;color:#555;padding-left:16px;line-height:36px">✉ Email Address</div>
    <div style="width:48px;background:var(--coral);display:flex;align-items:center;justify-content:center">
      <svg width="16" height="16" viewBox="0 0 24 24" fill="#fff"><path d="M2 12 22 3l-6 19-4-8z"/></svg>
    </div>
  </div>
  <div class="social" style="left:852px;top:167px"></div>
  <div class="social" style="left:892px;top:167px"></div>
  <div class="social" style="left:932px;top:167px"></div>
</footer>

</body>
</html>
```